Billboard Design for Modern Dispensary

Hello!
We need a eye-catching 12' x 24' billboard designed for a very successful, modern cannabis dispensary on the Oregon coast, United States. Because of rules, we cannot have any marijuana leafs or other cannabis related images (flower, joints, smoke, etc). We can use the words "Shop" or "Dispensary" - we cannot use the words "cannabis", "marijuana".

Some ideas we had are 3 words stacked on left or center of billboard - maybe across bottom we have horizontal logo and the following words - “South of bridge in Depoe Bay”
Another idea is to have a small bubble in bottom/top corner with image of our dog (face only) - with some words around it - like "BONUS Shop Dog" or "Cute Shop Dog" or "Best Shop Dog" or "Friendly Staff"

here's some 3 word examples:
ENJOY
YOUR
TRIP

or

FEEL
GOOD
JUST
AHEAD

or

GOOD
VIBES
ONLY

or

GOOD
TIMES
CHILL
VIBES

I have attached our logo. I have also included a stacked logo version (vertical, not horizontal). the formats are .EPS and .PDF - the logos were created in Affinity Design 2.x.

Our website is coralnook.net if you want to see more images, etc about our dispensary.

Artwork Requirements:
The billboard is 12' tall x 25' wide
The artwork needs to be 1”=1’ @ 300dpi
Please add 6” of bleed all around so your total artwork is 13”x26”
Final deliverable should be .Ai file.

Font styles to use
Sans Serif

Colors
0054AA
0677BA
7BADD7
CADEEF
E8F1F8

Requirements
Nice to have
• See the project description - we included some ideas to consider.
Should not have
• No cannabis images, like flower, cannabis leaves, paraphenlia, cartridges, joints, etc.

```html
<!DOCTYPE html>
<html lang="en">
<head>
<meta charset="utf-8">
<title>Coral Nook – Sleep Better Tonight</title>
<link rel="stylesheet" href="https://fonts.googleapis.com/css2?family=Poppins:wght@300;400;700;800&display=swap">
<style>
  :root {
    --green: #2a9a58;
    --gold: #b08a32;
    --blue: #3b9cd9;
    --ink: #141414;
    --paper: #ffffff;
    --tile-green: #dcebe0;
    --tile-gold: #efe6d2;
    --coat: #d9b27a;
    --coat-dark: #8a6a44;
  }
  html, body {
    margin: 0;
    padding: 0;
    overflow: hidden;
    background: var(--paper);
  }
  .billboard {
    position: relative;
    width: 1200px;
    height: 600px;
    background: var(--paper);
    overflow: hidden;
    font-family: "Poppins", Arial, sans-serif;
  }
  .pattern {
    position: absolute;
    left: 0;
    top: 0;
    width: 1200px;
    height: 600px;
  }
  .tile-green { fill: var(--tile-green); }
  .tile-gold { fill: var(--tile-gold); }

  .brand {
    position: absolute;
    left: 106px;
    top: 74px;
    width: 200px;
    display: flex;
    flex-direction: column;
    align-items: center;
  }
  .brand-dot {
    width: 56px;
    height: 56px;
    border-radius: 50%;
    background: var(--blue);
  }
  .brand-name {
    margin-top: 5px;
    font-weight: 300;
    font-size: 24px;
    letter-spacing: 0.5px;
    color: var(--blue);
    white-space: nowrap;
    line-height: 30px;
  }
  .brand-place {
    margin-top: 2px;
    display: flex;
    align-items: center;
    gap: 8px;
    font-weight: 400;
    font-size: 8px;
    letter-spacing: 3.5px;
    color: var(--ink);
    line-height: 10px;
  }
  .brand-place::before,
  .brand-place::after {
    content: "";
    width: 26px;
    height: 1px;
    background: var(--ink);
  }

  .headline {
    position: absolute;
    left: 128px;
    top: 190px;
    margin: 0;
    font-weight: 800;
    font-size: 100px;
    line-height: 116px;
    letter-spacing: -2px;
    white-space: nowrap;
  }
  .headline .line { display: block; }
  .c-green { color: var(--green); }
  .c-gold { color: var(--gold); }
  .c-blue { color: var(--blue); }

  .shop-dog {
    position: absolute;
    left: 861px;
    top: 227px;
    width: 250px;
    height: 250px;
  }
  .shop-dog svg { display: block; }
  .dog-label {
    font-family: "Poppins", Arial, sans-serif;
    font-weight: 700;
    font-size: 27px;
    fill: var(--blue);
  }
</style>
</head>
<body>
<main class="billboard">
  <svg class="pattern" viewBox="0 0 1200 600" role="img" aria-label="Staggered checkerboard pattern of the shop's brand mark in green, gold and black">
    <rect class="tile-green" x="459" y="8" width="81" height="97"/>
    <rect class="tile-gold" x="621" y="8" width="81" height="97"/>
    <rect class="tile-gold" x="945" y="8" width="81" height="97"/>
    <rect class="tile-green" x="1107" y="8" width="81" height="97"/>
    <rect class="tile-green" x="540" y="104" width="81" height="97"/>
    <rect class="tile-green" x="702" y="104" width="81" height="97"/>
    <rect class="tile-green" x="864" y="104" width="81" height="97"/>
    <rect class="tile-green" x="1026" y="104" width="81" height="97"/>
    <rect class="tile-gold" x="621" y="200" width="81" height="97"/>
    <rect class="tile-gold" x="783" y="200" width="81" height="97"/>
    <rect class="tile-gold" x="1107" y="200" width="81" height="97"/>
    <rect class="tile-green" x="702" y="297" width="81" height="97"/>
    <rect class="tile-green" x="783" y="394" width="81" height="97"/>
    <rect class="tile-gold" x="1107" y="394" width="81" height="97"/>
    <rect class="tile-gold" x="864" y="490" width="81" height="97"/>
    <rect class="tile-green" x="1026" y="490" width="81" height="97"/>
  </svg>

  <div class="brand">
    <div class="brand-dot"></div>
    <div class="brand-name">CORAL NOOK</div>
    <div class="brand-place">DEPOE BAY</div>
  </div>

  <h1 class="headline">
    <span class="line"><span class="c-green">S</span><span class="c-gold">LE</span><span class="c-green">E</span><span class="c-gold">P</span></span>
    <span class="line c-blue">BETTER</span>
    <span class="line"><span class="c-green">T</span><span class="c-blue">O</span><span class="c-gold">N</span><span class="c-blue">I</span><span class="c-green">G</span><span class="c-blue">H</span><span class="c-gold">T</span></span>
  </h1>

  <div class="shop-dog">
    <svg width="250" height="250" viewBox="0 0 250 250">
      <defs>
        <path id="label-arc" d="M 30 148 A 98 98 0 0 1 213 80"/>
        <radialGradient id="dog-tone" cx="50%" cy="45%" r="60%">
          <stop offset="0%" stop-color="var(--coat)"/>
          <stop offset="100%" stop-color="var(--coat-dark)"/>
        </radialGradient>
      </defs>
      <text class="dog-label"><textPath href="#label-arc">CUTE SHOP DOG</textPath></text>
      <path d="M 33 160 A 100 100 0 1 0 220 94" fill="none" stroke="var(--gold)" stroke-width="5"/>
      <circle cx="125" cy="125" r="75" fill="url(#dog-tone)" role="img" aria-label="Photo of the shop's fluffy golden dog"/>
    </svg>
  </div>
</main>
</body>
</html>
```